Design a business card
Business name: Kestrel Yield Consulting
Improving Business Profitibility

- An Overview of the Business & Service:

Business Performance Consulting

- The Target Market: Small to medium-sized business

- Design Specifics:
White card, blue ink, moon eclipse

No Logo

Target Market(s)

Small to medium-sized business

Font styles to use
Sans Serif

```html
<!DOCTYPE html>
<html lang="en">
<head>
<meta charset="utf-8">
<title>Kestrel Yield Consulting – Business Card</title>
<link rel="stylesheet" href="https://fonts.googleapis.com/css2?family=Poppins:wght@300;400;500;700&family=Montserrat:wght@400&display=swap">
<style>
  :root {
    --brand-blue: #0041c4;
    --ink-blue: #1639a8;
    --paper: #ffffff;
    --backdrop: #d9d9db;
    --tagline: #c9d6ff;
  }
  * { box-sizing: border-box; margin: 0; padding: 0; }
  html, body {
    width: 1200px; height: 1200px; overflow: hidden;
    background: var(--backdrop);
    font-family: "Poppins", sans-serif;
  }
  .sheet {
    width: 1200px; height: 1200px;
    display: flex; flex-direction: column; align-items: center; justify-content: center;
    gap: 70px;
  }
  .card {
    position: relative;
    width: 700px; height: 400px;
    box-shadow: 0 10px 30px rgba(0,0,0,0.15);
    overflow: hidden;
  }
  /* Front side */
  .card--front { background: var(--paper); color: var(--ink-blue); }
  .brand {
    position: absolute; display: flex; align-items: center; gap: 14px;
  }
  .brand__dot { border-radius: 50%; flex: none; }
  .brand__name { font-family: "Poppins", sans-serif; font-weight: 500; line-height: 1.1; }
  .card--front .brand { top: 44px; right: 48px; }
  .card--front .brand__dot { width: 54px; height: 54px; background: var(--brand-blue); }
  .card--front .brand__name { font-size: 22px; color: var(--brand-blue); }

  .holder { position: absolute; left: 48px; top: 220px; }
  .holder__name { font-size: 34px; line-height: 1; color: var(--brand-blue); letter-spacing: -0.5px; }
  .holder__first { font-weight: 300; }
  .holder__last { font-weight: 700; }
  .holder__role { margin-top: 6px; font-size: 13px; font-weight: 500; letter-spacing: 0.5px; }

  .contacts {
    position: absolute; left: 48px; right: 48px; bottom: 40px;
    display: grid; grid-template-columns: 1fr 1.3fr; row-gap: 12px; column-gap: 30px;
    list-style: none;
  }
  .contacts__item { display: flex; align-items: center; gap: 10px; font-size: 14px; }
  .contacts__icon { width: 22px; height: 22px; flex: none; }
  .front-band {
    position: absolute; left: 0; bottom: 0; width: 73%; height: 14px; background: var(--brand-blue);
  }

  /* Back side */
  .card--back { background: var(--brand-blue); color: var(--paper); }
  .card--back .brand { top: 150px; left: 50%; transform: translateX(-50%); }
  .card--back .brand__dot { width: 80px; height: 80px; background: var(--paper); }
  .card--back .brand__name { font-size: 32px; white-space: nowrap; }
  .tagline {
    position: absolute; right: 48px; bottom: 44px;
    font-family: "Montserrat", sans-serif; font-size: 15px; letter-spacing: 2.5px;
    color: var(--tagline);
  }
</style>
</head>
<body>
<main class="sheet">
  <section class="card card--front" aria-label="Card front">
    <div class="brand">
      <span class="brand__dot"></span>
      <span class="brand__name">Kestrel Yield<br>Consulting</span>
    </div>

    <div class="holder">
      <p class="holder__name"><span class="holder__first">DESMOND </span><span class="holder__last">HALE</span></p>
      <p class="holder__role">DIRECTOR</p>
    </div>

    <ul class="contacts">
      <li class="contacts__item">
        <svg class="contacts__icon" viewBox="0 0 22 22" aria-hidden="true">
          <circle cx="11" cy="11" r="10" fill="none" stroke="currentColor" stroke-width="1.4"/>
          <path d="M7.5 6.5l2 0 1 2.5-1.3 1c.6 1.3 1.5 2.2 2.8 2.8l1-1.3 2.5 1v2c-4.5.3-8.3-3.5-8-8z" fill="currentColor"/>
        </svg>
        <span>555.014.2290</span>
      </li>
      <li class="contacts__item">
        <svg class="contacts__icon" viewBox="0 0 22 22" aria-hidden="true">
          <circle cx="11" cy="11" r="10" fill="none" stroke="currentColor" stroke-width="1.4"/>
          <circle cx="9" cy="11" r="2.6" fill="none" stroke="currentColor" stroke-width="1.5"/>
          <circle cx="13" cy="11" r="2.6" fill="none" stroke="currentColor" stroke-width="1.5"/>
        </svg>
        <span>www.kestrelyield.com</span>
      </li>
      <li class="contacts__item">
        <svg class="contacts__icon" viewBox="0 0 22 22" aria-hidden="true">
          <circle cx="11" cy="11" r="10" fill="none" stroke="currentColor" stroke-width="1.4"/>
          <rect x="6" y="7.5" width="10" height="7" rx="1" fill="currentColor"/>
          <path d="M6.5 8l4.5 3.5 4.5-3.5" fill="none" stroke="#fff" stroke-width="1"/>
        </svg>
        <span>info@kestrelyield.com</span>
      </li>
      <li class="contacts__item">
        <svg class="contacts__icon" viewBox="0 0 22 22" aria-hidden="true">
          <circle cx="11" cy="11" r="10" fill="none" stroke="currentColor" stroke-width="1.4"/>
          <path d="M11 5.5a3.6 3.6 0 0 1 3.6 3.6c0 2.6-3.6 6.6-3.6 6.6s-3.6-4-3.6-6.6A3.6 3.6 0 0 1 11 5.5z" fill="currentColor"/>
          <circle cx="11" cy="9.1" r="1.2" fill="#fff"/>
        </svg>
        <span>48 Harlow St, Brookfield, NJ 07045</span>
      </li>
    </ul>
    <div class="front-band"></div>
  </section>

  <section class="card card--back" aria-label="Card back">
    <div class="brand">
      <span class="brand__dot"></span>
      <span class="brand__name">Kestrel Yield<br>Consulting</span>
    </div>
    <p class="tagline">BUSINESS - PERFORMANCE - CONSULTING</p>
  </section>
</main>
</body>
</html>
```